Marisol Specialty Coffee needs a Packaging design

We need packaging design for coffee that suits our brand identity, that is the best quality in Mexico.
We only sell mexican coffee with Q scores above 80
We are evaluating 3 types of packaging: Bag, Box and Cillinder can
The specific package format will be decided based on the designs that we get.
Updates

Target Market(s)

Coffee experts and enthusiast.
People that relate the Coffee consumption and experience with wine tasting and Bon Vivant way

Requirements
Should not have
• Photos any mexican cliché

```html
<!DOCTYPE html>
<html lang="en">
<head>
<meta charset="utf-8">
<title>Marisol Specialty Coffee – Dark Roast Bag</title>
<link rel="stylesheet" href="https://fonts.googleapis.com/css2?family=Questrial&display=swap">
<style>
  :root {
    --backdrop: #ecebe9;
    --bag-black: #0d0d0e;
    --bag-sheen: #232326;
    --gold: #b48a3e;
    --gold-light: #e3c47c;
    --gold-dark: #7a5a24;
    --gold-fade: rgba(122, 90, 36, 0);
    --white: #f7f6f3;
    --zip-line: #2c2c30;
  }
  * { margin: 0; padding: 0; box-sizing: border-box; }
  html, body {
    width: 1200px;
    height: 1200px;
    overflow: hidden;
    background: var(--backdrop);
  }
  .canvas {
    position: relative;
    width: 1200px;
    height: 1200px;
    font-family: "Questrial", sans-serif;
  }
  .bag-front {
    position: absolute;
    left: 210px;
    top: 40px;
    width: 780px;
    height: 1120px;
    border-radius: 10px;
    background: linear-gradient(120deg, var(--bag-sheen) 0%, var(--bag-black) 35%, var(--bag-black) 70%, var(--bag-sheen) 100%);
    overflow: hidden;
  }
  .zip-seal {
    position: absolute;
    left: 0;
    top: 120px;
    width: 100%;
    height: 14px;
    border-top: 2px solid var(--zip-line);
    border-bottom: 2px solid var(--zip-line);
  }
  .brand {
    position: absolute;
    left: 80px;
    top: 250px;
    display: flex;
    align-items: center;
    gap: 16px;
    color: var(--gold);
    font-size: 30px;
    letter-spacing: 0.5px;
  }
  .brand-dot {
    width: 40px;
    height: 40px;
    border-radius: 50%;
    background: var(--gold);
  }
  .steam-illustration {
    position: absolute;
    left: 60px;
    top: 320px;
    width: 680px;
    height: 560px;
    background: radial-gradient(ellipse closest-side at 58% 48%,
      var(--gold-light) 0%,
      var(--gold) 38%,
      var(--gold-dark) 68%,
      var(--gold-fade) 100%);
  }
  .product-name {
    position: absolute;
    left: 70px;
    top: 790px;
    color: var(--white);
    font-size: 178px;
    line-height: 1;
    letter-spacing: -2px;
  }
  .roast-level {
    position: absolute;
    left: 80px;
    top: 970px;
    color: var(--gold);
    font-size: 104px;
    line-height: 1;
    letter-spacing: 1px;
  }
</style>
</head>
<body>
  <div class="canvas">
    <div class="bag-front">
      <div class="zip-seal"></div>
      <div class="brand">
        <span class="brand-dot"></span>
        <span class="brand-name">Marisol Specialty Coffee</span>
      </div>
      <div class="steam-illustration" role="img" aria-label="Gold line illustration of a coffee cup with ornate swirling steam rising from it"></div>
      <div class="product-name">COFFEE</div>
      <div class="roast-level">DARK ROAST</div>
    </div>
  </div>
</body>
</html>
```